Flyer Template

I need a flyer template for door knocking on properties. Text Boxes need to be editable, with a header and text body. Footer to be my info. Project to be stylized to match my real estate signs and logo art from past projects

```html
<!DOCTYPE html>
<html lang="en">
<head>
<meta charset="UTF-8">
<title>Property Flyer</title>
<link rel="stylesheet" href="https://fonts.googleapis.com/css2?family=Cinzel:wght@700;900&family=Montserrat:wght@600;700&family=Source+Sans+3:wght@400;600&display=swap">
<style>
  :root {
    --stage: #777777;
    --paper: #ffffff;
    --brand-red: #ec1c24;
    --ink: #2b2b2b;
    --ink-soft: #333333;
    --footer: #1e1e1e;
    --frame: #ffffff;
    --sky: #6aa3e6;
    --sky-pale: #b9d5f0;
    --water: #4f86c0;
    --foliage: #3f6b2c;
    --foliage-dark: #2c4f22;
    --lawn: #6ea843;
    --brick: #8a4a38;
    --wood: #9a5a26;
    --wood-dark: #5a2f15;
    --cream: #e6d6bd;
  }
  * { box-sizing: border-box; margin: 0; padding: 0; }
  html, body { width: 990px; height: 1200px; overflow: hidden; background: var(--stage); }
  .flyer {
    position: absolute; left: 53px; top: 28px;
    width: 883px; height: 1143px;
    background: var(--paper);
    box-shadow: 0 10px 30px rgba(0,0,0,.35);
    overflow: hidden;
  }
  .hero-photo {
    position: absolute; left: 0; top: 0; width: 883px; height: 431px;
    background:
      radial-gradient(ellipse 190px 130px at 330px 250px, rgba(138,74,56,.85) 0%, rgba(138,74,56,.4) 55%, rgba(138,74,56,0) 100%),
      radial-gradient(ellipse 200px 70px at 800px 240px, rgba(79,134,192,.95) 0%, rgba(79,134,192,.6) 60%, rgba(79,134,192,0) 100%),
      radial-gradient(ellipse 160px 260px at 40px 320px, rgba(44,79,34,.9) 0%, rgba(44,79,34,0) 100%),
      radial-gradient(ellipse 260px 80px at 620px 400px, rgba(110,168,67,.9) 0%, rgba(110,168,67,0) 100%),
      linear-gradient(180deg, var(--sky) 0%, var(--sky-pale) 38%, var(--foliage) 58%, var(--foliage-dark) 78%, var(--lawn) 100%);
  }
  .agency-name {
    position: absolute; left: 578px; top: 48px;
    font: 600 23px/1 "Montserrat", sans-serif;
    color: #4a4a4a; letter-spacing: .3px;
  }
  .headline-band {
    position: absolute; left: 0; top: 431px; width: 883px; height: 128px;
    background: var(--brand-red);
  }
  .headline {
    position: absolute; left: 68px; top: 446px; width: 500px;
    font: 700 35px/33px "Cinzel", serif;
    color: #ffffff; letter-spacing: 1px;
  }
  .interior-photo {
    position: absolute; left: 576px; width: 240px; height: 168px;
    border: 2px solid var(--frame);
  }
  .interior-photo::after {
    content: ""; position: absolute; inset: 5px;
    border: 1.5px solid var(--frame);
  }
  .interior-photo.music-room {
    top: 412px;
    background:
      radial-gradient(ellipse 60px 40px at 35px 60px, rgba(190,215,235,.9) 0%, rgba(190,215,235,0) 100%),
      radial-gradient(ellipse 60px 40px at 205px 60px, rgba(190,215,235,.9) 0%, rgba(190,215,235,0) 100%),
      radial-gradient(ellipse 80px 45px at 115px 95px, rgba(40,25,20,.85) 0%, rgba(40,25,20,0) 100%),
      linear-gradient(180deg, var(--cream) 0%, #c9a67a 50%, #b06a30 75%, var(--wood-dark) 100%);
  }
  .interior-photo.foyer {
    top: 600px;
    background:
      radial-gradient(ellipse 50px 30px at 120px 40px, rgba(255,220,160,.8) 0%, rgba(255,220,160,0) 100%),
      radial-gradient(ellipse 40px 60px at 120px 95px, rgba(200,130,70,.9) 0%, rgba(200,130,70,0) 100%),
      linear-gradient(180deg, #6a3514 0%, var(--wood) 40%, #c47a3a 75%, #8a4a1e 100%);
  }
  .body-copy {
    position: absolute; left: 68px; top: 578px; width: 448px;
    font: 400 16px/19px "Source Sans 3", sans-serif;
    color: var(--ink-soft);
  }
  .features {
    position: absolute; left: 68px; top: 734px; list-style: none;
    font: 600 19.5px/27px "Source Sans 3", sans-serif;
    color: var(--ink);
  }
  .features li { display: flex; align-items: center; gap: 12px; }
  .features svg { width: 14px; height: 14px; flex: none; }
  .agent-name-bar {
    position: absolute; left: 68px; top: 888px; width: 463px; height: 56px;
    background: var(--brand-red);
    font: 700 38px/56px "Montserrat", sans-serif;
    color: #ffffff; text-align: center; letter-spacing: .5px;
  }
  .contact-line { position: absolute; left: 70px; display: flex; align-items: center; gap: 12px; color: var(--ink); }
  .contact-line svg { width: 42px; height: 42px; flex: none; }
  .contact-line.phone { top: 953px; font: 700 50px/1 "Montserrat", sans-serif; letter-spacing: .5px; }
  .contact-line.email { top: 1004px; font: 600 25px/1 "Montserrat", sans-serif; letter-spacing: 1px; }
  .brokerage {
    position: absolute; left: 565px; top: 836px; width: 260px; text-align: center;
  }
  .brokerage-mark { width: 100px; height: 100px; margin: 0 auto 36px; background: var(--brand-red); }
  .brokerage-name {
    font: 700 42px/40px "Montserrat", sans-serif; color: #000000;
  }
  .footer-bar {
    position: absolute; left: 28px; top: 1059px; width: 830px; height: 56px;
    background: var(--footer);
    font: 600 21px/56px "Montserrat", sans-serif;
    color: #ffffff; text-align: center; letter-spacing: .5px;
  }
</style>
</head>
<body>
  <main class="flyer">
    <div class="hero-photo" role="img" aria-label="Aerial photo of a large brick Victorian home on a lawn above a bay"></div>
    <div class="agency-name">HARBOR CREST GROUP</div>

    <div class="headline-band"></div>
    <h1 class="headline">Lorem ipsum dolor<br>sit amet, consectetur<br>adipiscing elit</h1>

    <div class="interior-photo music-room" role="img" aria-label="Interior photo of a sunlit room with a grand piano"></div>
    <div class="interior-photo foyer" role="img" aria-label="Interior photo of a wood-panelled entrance hall"></div>

    <p class="body-copy">Lorem ipsum dolor sit amet, consectetur adipiscing elit, sed do eiusmod tempor incididunt ut labore et dolore magna aliqua. Ut enim ad minim veniam, quis nostrud exercitation ullamco laboris nisi ut aliquip ex ea commodo consequat. Duis aute irure dolor in reprehenderit in voluptate velit esse cillum dolore eu fugiat nulla pariatur. Excepteur sint occaecat cupidatat non proident, sunt in culpa qui officia deserunt mollit anim id est laborum.</p>

    <ul class="features">
      <li><svg viewBox="0 0 14 14"><path d="M1.5 7.5l3.5 3.5 7.5-8" fill="none" stroke="#ec1c24" stroke-width="2.4"/></svg>Sed ut perspiciatis unde omnis</li>
      <li><svg viewBox="0 0 14 14"><path d="M1.5 7.5l3.5 3.5 7.5-8" fill="none" stroke="#ec1c24" stroke-width="2.4"/></svg>iste natus error sit voluptatem accusantium dolor</li>
      <li><svg viewBox="0 0 14 14"><path d="M1.5 7.5l3.5 3.5 7.5-8" fill="none" stroke="#ec1c24" stroke-width="2.4"/></svg>laudantium, totam rem aperiam, eaque ipsa</li>
      <li><svg viewBox="0 0 14 14"><path d="M1.5 7.5l3.5 3.5 7.5-8" fill="none" stroke="#ec1c24" stroke-width="2.4"/></svg>quae ab illo inventore veritatis et quasi</li>
      <li><svg viewBox="0 0 14 14"><path d="M1.5 7.5l3.5 3.5 7.5-8" fill="none" stroke="#ec1c24" stroke-width="2.4"/></svg>architecto beatae vitae dicta sunt explicabo</li>
    </ul>

    <div class="agent-name-bar">JORDAN WHITLEY</div>
    <div class="contact-line phone">
      <svg viewBox="0 0 42 42"><circle cx="21" cy="21" r="21" fill="#ec1c24"/><path d="M14 11c1.5-1 3 0 4 2l1.2 2.8c.4 1-.1 2-1 2.6l-1.2.8c1 2.6 3 4.6 5.6 5.8l.9-1.2c.6-.9 1.700-1.3 2.6-.9l2.8 1.2c2 .9 3 2.4 2 3.9-1.5 2.3-4 3-6.5 2-5.6-2.3-9.5-6.2-11.6-11.5-1-2.600-.3-5.3 1.2-7.5z" fill="none" stroke="#ffffff" stroke-width="1.8"/></svg>
      <span>555-014-0287</span>
    </div>
    <div class="contact-line email">
      <svg viewBox="0 0 42 42"><circle cx="21" cy="21" r="21" fill="#ec1c24"/><rect x="11" y="14" width="20" height="14" fill="none" stroke="#ffffff" stroke-width="1.8"/><path d="M11 14l10 8 10-8" fill="none" stroke="#ffffff" stroke-width="1.8"/></svg>
      <span>JWHITLEY@MAILBOX.COM</span>
    </div>

    <div class="brokerage">
      <div class="brokerage-mark"></div>
      <div class="brokerage-name">WHITLEY<br>REALTY</div>
    </div>

    <footer class="footer-bar">EACH OFFICE INDEPENDENTLY OWNED AND OPERATED</footer>
  </main>
</body>
</html>
```